Ridgeline Sawcutting, Inc. Business Card

Create a business card that is eye catching and based around concrete sawcutting. I've attached our current business card and logo for reference. We like aspects of the current business card, but it is starting to feel very loud and lost. We would like something that is still fun but is more modern and streamlined.

```html
<!DOCTYPE html>
<html lang="en">
<head>
<meta charset="utf-8">
<title>Ridgeline Sawcutting, Inc. Business Card</title>
<link rel="stylesheet" href="https://fonts.googleapis.com/css2?family=Audiowide&family=Lato:wght@400;700;900&family=Roboto+Slab:wght@800&display=swap">
<style>
  :root {
    --navy: #102464;
    --navy-deep: #0b1b4e;
    --red: #d21f2b;
    --gold: #f5c400;
    --silver-light: #ececec;
    --silver-mid: #c9c9c9;
    --silver-dark: #a9a9a9;
    --white: #ffffff;
    --page: #2b2b2d;
  }
  * { box-sizing: border-box; margin: 0; padding: 0; }
  html, body { width: 1200px; height: 982px; overflow: hidden; }
  body {
    background: var(--page);
    font-family: "Lato", sans-serif;
    position: relative;
  }
  .card {
    position: absolute;
    left: 290px;
    width: 620px;
    height: 354px;
    border-radius: 22px;
    overflow: hidden;
    box-shadow: 0 14px 30px rgba(0,0,0,.45);
  }

  /* ---------- front ---------- */
  .card-front { top: 70px; }
  .plate-texture {
    position: absolute; inset: 0;
    background: linear-gradient(135deg, var(--silver-light) 0%, var(--silver-mid) 55%, var(--silver-dark) 100%);
  }
  .brand {
    position: absolute; left: 40px; top: 52px; width: 230px;
    display: flex; flex-direction: column; align-items: center; gap: 16px;
  }
  .brand-dot {
    width: 170px; height: 170px; border-radius: 50%;
    background: var(--navy);
  }
  .brand-name {
    font-family: "Lato", sans-serif; font-weight: 900;
    font-size: 19px; letter-spacing: .08em; color: var(--navy);
    text-align: center; line-height: 1.2;
  }
  .service-column {
    position: absolute; right: 0; top: 0; bottom: 0; left: 300px;
    display: flex; align-items: stretch;
  }
  .vertical-text {
    writing-mode: vertical-rl;
    transform: rotate(180deg);
    white-space: nowrap;
  }
  .hotline {
    width: 62px; display: flex; align-items: center; justify-content: center;
    font-family: "Roboto Slab", serif; font-weight: 800;
    font-size: 30px; color: var(--navy);
  }
  .band {
    flex: 1; margin: 0 3px;
    background: var(--navy);
    border-left: 3px solid var(--red);
    border-right: 3px solid var(--red);
    display: flex; align-items: center; justify-content: center;
    color: var(--gold); font-weight: 700; font-size: 29px; letter-spacing: .01em;
  }
  .band-small { font-size: 21px; }
  .band:last-child { margin-right: 0; }

  /* ---------- back ---------- */
  .card-back { top: 520px; background: var(--navy); }
  .holder-name {
    position: absolute; left: 44px; top: 34px;
    font-family: "Audiowide", sans-serif; font-size: 36px; letter-spacing: .02em;
    background: linear-gradient(180deg, #ffffff 0%, #9fa3ab 55%, #e4e4e4 100%);
    -webkit-background-clip: text; background-clip: text; color: transparent;
  }
  .contact-list {
    position: absolute; left: 44px; top: 100px; list-style: none;
    color: var(--white); font-size: 18px; line-height: 1.3;
  }
  .contact-list li { display: flex; gap: 10px; align-items: flex-start; margin-bottom: 4px; }
  .contact-list svg { width: 16px; height: 16px; flex: none; margin-top: 3px; fill: var(--red); }
  .company { color: var(--gold); font-weight: 700; }
  .vanity { color: var(--gold); font-weight: 900; font-size: 21px; }
  .contact-block { display: block; }
  .mascot-art {
    position: absolute; right: 0; bottom: 0; width: 300px; height: 300px;
    border-top-left-radius: 150px;
    background: radial-gradient(circle at 60% 55%, #ffffff 0%, #e8e9ee 50%, #c7cad4 100%);
  }
</style>
</head>
<body>

<section class="card card-front">
  <div class="plate-texture" role="img" aria-label="Brushed diamond-plate steel texture background"></div>
  <div class="brand">
    <div class="brand-dot"></div>
    <div class="brand-name">RIDGELINE SAWCUTTING</div>
  </div>
  <div class="service-column">
    <div class="hotline vertical-text">(855)-CUTLINE</div>
    <div class="band vertical-text">WALL SAWING</div>
    <div class="band vertical-text">CORE DRILLING</div>
    <div class="band vertical-text">SLAB SAWING</div>
    <div class="band band-small vertical-text">BREAKING &amp; REMOVAL</div>
  </div>
</section>

<section class="card card-back">
  <h1 class="holder-name">DANA MARLOWE</h1>
  <ul class="contact-list">
    <li>
      <svg viewBox="0 0 16 16"><path d="M8 0a5.5 5.5 0 0 0-5.5 5.5C2.5 10 8 16 8 16s5.5-6 5.5-10.5A5.5 5.5 0 0 0 8 0zm0 8a2.5 2.5 0 1 1 0-5 2.5 2.5 0 0 1 0 5z"/></svg>
      <span><span class="contact-block company">Ridgeline Sawcutting, Inc.</span>
      <span class="contact-block">48 Harmon Ave</span>
      <span class="contact-block">Fairview, NJ 07022</span></span>
    </li>
    <li>
      <svg viewBox="0 0 16 16"><path d="M3.6 1l2.6 3-1.5 1.8a9 9 0 0 0 5.5 5.5l1.8-1.5 3 2.6-1.6 2.3C7.6 14.4 1.6 8.4 1.3 2.6z"/></svg>
      <span class="vanity">(855) CUTLINE</span>
    </li>
    <li>
      <svg viewBox="0 0 16 16"><path d="M3.6 1l2.6 3-1.5 1.8a9 9 0 0 0 5.5 5.5l1.8-1.5 3 2.6-1.6 2.3C7.6 14.4 1.6 8.4 1.3 2.6z"/></svg>
      <span>(855) 555-0142</span>
    </li>
    <li>
      <svg viewBox="0 0 16 16"><path d="M4 0h8a1.5 1.5 0 0 1 1.5 1.5v13A1.5 1.5 0 0 1 12 16H4a1.5 1.5 0 0 1-1.5-1.5v-13A1.5 1.5 0 0 1 4 0zm0 2v10h8V2z"/></svg>
      <span>(973) 555-0187</span>
    </li>
    <li>
      <svg viewBox="0 0 16 16"><path d="M0 3h16v1.2L8 9 0 4.2zm0 2.8l8 4.8 8-4.8V13H0z"/></svg>
      <span>Dana@RidgelineSawcutting.com</span>
    </li>
    <li>
      <svg viewBox="0 0 16 16"><path d="M8 0a8 8 0 1 0 0 16A8 8 0 0 0 8 0zm5.9 7h-2.5a12 12 0 0 0-1.2-5A6 6 0 0 1 13.9 7zM8 2c.8 1.2 1.3 3 1.4 5H6.6C6.7 5 7.2 3.2 8 2zM5.8 2a12 12 0 0 0-1.2 5H2.1a6 6 0 0 1 3.7-5zM2.1 9h2.5a12 12 0 0 0 1.2 5A6 6 0 0 1 2.1 9zM8 14c-.8-1.2-1.3-3-1.4-5h2.8c-.1 2-.6 3.8-1.4 5zm2.2 0a12 12 0 0 0 1.2-5h2.5a6 6 0 0 1-3.7 5z"/></svg>
      <span>RidgelineSawcutting.com</span>
    </li>
  </ul>
  <div class="mascot-art" role="img" aria-label="Illustration of a bald eagle head in white, black and yellow"></div>
</section>

</body>
</html>
```